Ledgerwise Business Card Design

Business Card Design for new business called Ledgerwise focused on selling business software to small and medium size companies who have outgrown Tallymark. Similar companies would be Tallymark, Nuvo, CoreFlow. Also Dealharbor would be good to look at for additional ideas around look and feel.

Target Market(s)

Business to Business

Industry/Entity Type

Information Technology

Contact Information for Business Card

Standard Business Card Information

Font styles to use
Sans Serif

```html
<!DOCTYPE html>
<html lang="en">
<head>
<meta charset="utf-8">
<title>Ledgerwise Business Card</title>
<link rel="stylesheet" href="https://fonts.googleapis.com/css2?family=Open+Sans:wght@400;600;700;800&display=swap">
<style>
  :root {
    --bg: #2b2b2b;
    --card: #131313;
    --card-edge: #1c1c1c;
    --orange: #f7941d;
    --blue: #1d5d97;
    --text: #e8e8e8;
    --muted: #bdbdbd;
    --divider: #242424;
  }
  * { box-sizing: border-box; margin: 0; padding: 0; }
  html, body { width: 1200px; height: 900px; overflow: hidden; }
  body {
    background: var(--bg);
    font-family: "Open Sans", sans-serif;
    display: flex;
    align-items: center;
    justify-content: center;
    gap: 60px;
  }
  .card {
    width: 500px;
    height: 286px;
    background: var(--card);
    border: 1px solid var(--card-edge);
    border-radius: 18px;
    position: relative;
    overflow: hidden;
  }
  /* Front */
  .card-front { display: flex; }
  .front-mark {
    width: 50%;
    display: flex;
    align-items: center;
    justify-content: center;
    border-right: 1px solid var(--divider);
  }
  .mark-circle {
    width: 130px; height: 130px;
    border-radius: 50%;
    background: var(--orange);
  }
  .front-details {
    width: 50%;
    padding: 40px 0 0 30px;
    color: var(--text);
  }
  .person-name {
    color: var(--orange);
    font-weight: 700;
    font-size: 17px;
    line-height: 1.1;
  }
  .person-title { font-size: 12.5px; margin-bottom: 18px; }
  .address { font-size: 12.5px; line-height: 1.3; margin-bottom: 18px; }
  .contact-list { list-style: none; font-size: 12.5px; }
  .contact-list li { display: flex; align-items: center; gap: 10px; line-height: 1.55; }
  .contact-list svg { width: 10px; height: 10px; fill: var(--orange); flex: none; }
  /* Back */
  .card-back { display: flex; flex-direction: column; align-items: center; justify-content: center; }
  .brand { display: flex; align-items: center; gap: 12px; margin-top: -10px; }
  .brand-dot { width: 26px; height: 26px; border-radius: 50%; background: var(--orange); }
  .brand-name {
    color: var(--blue);
    font-weight: 800;
    font-size: 34px;
    letter-spacing: -0.5px;
    text-transform: uppercase;
  }
  .back-web {
    position: absolute;
    right: 90px;
    bottom: 62px;
    color: var(--orange);
    font-weight: 700;
    font-size: 12px;
  }
</style>
</head>
<body>
  <section class="card card-front" aria-label="Card front">
    <div class="front-mark"><div class="mark-circle"></div></div>
    <div class="front-details">
      <p class="person-name">Daniel Brooks</p>
      <p class="person-title">Managing Director</p>
      <p class="address">12345, Address Goes Here<br>Country Name, 123456</p>
      <ul class="contact-list">
        <li><svg viewBox="0 0 10 10"><path d="M2 0h2l1 3-1.5 1a6 6 0 0 0 2.5 2.5L7 5l3 1v2c0 1-1 2-2 2A8 8 0 0 1 0 2c0-1 1-2 2-2z"/></svg>(044)-456-7890</li>
        <li><svg viewBox="0 0 10 10"><path d="M2 0h5v3H2zM0 3h10v6H0zM2 5v1h2V5zm4 0v1h2V5z"/></svg>123-456-7890</li>
        <li><svg viewBox="0 0 10 10"><path d="M0 2h10v1L5 6 0 3zm0 2 5 3 5-3v4H0z"/></svg>info@ledgerwise.com</li>
        <li><svg viewBox="0 0 10 10"><path d="M4 6 6 4M3.5 4.5 2 6a1.4 1.4 0 0 0 2 2l1.5-1.5M6.5 5.5 8 4a1.4 1.4 0 0 0-2-2L4.5 3.5" fill="none" stroke="#f7941d" stroke-width="1.4"/></svg>www.ledgerwise.com</li>
      </ul>
    </div>
  </section>

  <section class="card card-back" aria-label="Card back">
    <div class="brand">
      <span class="brand-dot"></span>
      <span class="brand-name">Ledgerwise</span>
    </div>
    <p class="back-web">www.ledgerwise.com</p>
  </section>
</body>
</html>
```